Corvale Mechanical - Letterhead

We are a plumbing and hvac company based in Calgary. This letterhead will be on our quotes, invoices, preventative maintenance proposals etc.

```html
<!DOCTYPE html>
<html lang="en">
<head>
<meta charset="utf-8">
<title>Corvale Mechanical – Letterhead</title>
<link href="https://fonts.googleapis.com/css2?family=Figtree:ital,wght@0,400;0,600;0,800;1,700&family=Work+Sans:wght@400&display=swap" rel="stylesheet">
<style>
  :root{
    --backdrop:#ececec;
    --paper:#ffffff;
    --brand-blue:#1f6db5;
    --brand-orange:#e8592a;
    --ink-dark:#4a4a4a;
    --ink-body:#7a7a7a;
    --ink-contact:#2b2b2b;
    --signature-tone:#e4e4e4;
  }
  *{margin:0;padding:0;box-sizing:border-box}
  html,body{width:1185px;height:1200px;overflow:hidden;background:var(--backdrop)}
  .letterhead{
    position:absolute;left:189px;top:30px;width:806px;height:1140px;
    background:var(--paper);
    font-family:"Figtree",sans-serif;
  }
  .brand{
    position:absolute;left:78px;top:118px;
    display:flex;align-items:center;gap:8px;
  }
  .brand-dot{width:14px;height:14px;border-radius:50%;background:var(--brand-orange)}
  .brand-name{
    font-family:"Figtree",sans-serif;font-weight:800;font-size:19px;
    letter-spacing:.5px;color:var(--brand-blue);text-transform:uppercase;
  }
  .contact{
    position:absolute;left:374px;top:120px;
    font-family:"Work Sans",sans-serif;font-size:12.5px;line-height:16.5px;color:var(--ink-contact);
    list-style:none;
  }
  .contact li{display:flex;align-items:center;gap:5px}
  .contact svg{width:8px;height:8px;flex:none}
  .address{
    position:absolute;left:593px;top:136px;
    font-family:"Work Sans",sans-serif;font-size:12.5px;line-height:16.5px;color:var(--ink-contact);
    font-style:normal;
  }
  .header-rule{position:absolute;left:78px;top:192px;width:652px;height:1.5px;background:var(--brand-orange)}
  .salutation{
    position:absolute;left:78px;top:301px;
    font-size:21px;font-weight:600;color:var(--ink-dark);
  }
  .body-copy{
    position:absolute;left:78px;width:652px;
    font-size:12.1px;line-height:20.4px;color:var(--ink-body);
    text-align:justify;text-align-last:justify;
  }
  .p1{top:353px}.p2{top:463px}.p3{top:551px}.p4{top:780px}
  .signatory{position:absolute;left:78px;top:847px;color:var(--ink-dark)}
  .signatory-name{font-size:21px;font-weight:700;font-style:italic;line-height:24px}
  .signatory-role{font-size:11.5px;font-weight:700;font-style:italic}
  .signature{
    position:absolute;left:78px;top:916px;width:208px;height:68px;
    background:linear-gradient(90deg,var(--signature-tone),#f4f4f4);
    border-radius:4px;
  }
</style>
</head>
<body>
<main class="letterhead">
  <div class="brand">
    <span class="brand-dot"></span>
    <span class="brand-name">Corvale Mechanical</span>
  </div>

  <ul class="contact">
    <li><svg viewBox="0 0 10 10"><path d="M2 1 L4 1 L4.6 3 L3.4 4 Q4.5 6 6 6.6 L7 5.4 L9 6 L9 8 Q5 9 2 5 Q1 3 2 1Z" fill="var(--brand-blue)"/></svg>(403) 555-0148</li>
    <li><svg viewBox="0 0 10 10"><rect x="1" y="2" width="8" height="6" fill="none" stroke="var(--brand-blue)" stroke-width="1.2"/><path d="M1 2 L5 5.5 L9 2" fill="none" stroke="var(--brand-blue)" stroke-width="1.2"/></svg>info@corvalemech.com</li>
    <li><svg viewBox="0 0 10 10"><circle cx="5" cy="5" r="4" fill="none" stroke="var(--brand-blue)" stroke-width="1.1"/><path d="M1 5 H9 M5 1 Q2.5 5 5 9 Q7.5 5 5 1" fill="none" stroke="var(--brand-blue)" stroke-width=".9"/></svg>www.corvalemech.com</li>
  </ul>

  <address class="address">2210 Ridgeway Road<br>Calgary, AB T2P 1J9</address>

  <div class="header-rule"></div>

  <h1 class="salutation">Dear sir/Madam,</h1>

  <p class="body-copy p1">Lorem Ipsum is simply dummy text of the printing and typesetting industry. Lorem Ipsum has been the indus-try's standard dummy text ever since the 1500s, when an unknown printer took a galley of type and scrambled it to make a type specimen book. It has survived not only five centuries, but also the leap into electronic typesetting, remaining essentially unchanged. It was popularised in the 1960s with the release of Lettrapress</p>

  <p class="body-copy p2">of type and scrambled it to make a type specimen book. It has survived not only five centuries, but also the leap into electronic typesetting, remaining essentially unchanged. It was popularised in the 1960s with the release of Lettrapress sheets containing Lorem Ipsum passages, and more recently with desktop publishing software like</p>

  <p class="body-copy p3">Contrary to popular belief, Lorem Ipsum is not simply random text. It has roots in a piece of classical Latin litera-ture from 45 BC, making it over 2000 years old. Harold Brennick, a Latin professor at Ashford Hill College in Vermont, looked up one of the more obscure Latin words, consectetur, from a Lorem Ipsum passage, and going through the cites of the word in classical literature, discovered the undoubtable source. Lorem Ipsum comes from sections 1.10.32 and 1.10.33 of "de Finibus Bonorum et Malorum" (The Extremes of Good and Evil) by Tullian, written in 45 BC. This book is a treatise on the theory of ethics, very popular during the Renaissance. The first line of Lorem Ipsum, "Lorem ipsum dolor sit amet..", comes from a line in section 1.10.32. typesetting, remaining essentially unchanged. It was popularised in the 1960s with the release of Lettrapress sheets containing Lorem Ipsum passages, and more recently with desktop publishing software like Folio Page There are many variations of passages of Lorem Ipsum available, but the majority have suffered alteration in</p>

  <p class="body-copy p4">some form, by injected humour, or randomised words which don't look even slightly believable. If you are going to use a passage of Lorem Ipsum, you need to be sure there isn't anything embarrassing hidden in the middle</p>

  <div class="signatory">
    <p class="signatory-name">Dana Whitlock</p>
    <p class="signatory-role">Director</p>
  </div>

  <div class="signature" role="img" aria-label="Handwritten signature of the director"></div>
</main>
</body>
</html>
```